Mandala-like Graphic for Ecosystem of Well-Being

I have created a simple graphic for a framework I use with clients and potential clients. I would like it to look more polished, professional, and customized. (As opposed to non-graphic designer created it on Canva or Powrepoint) I would like to possibly integrate my brand colors---or one of my brand colors. https://huechartly.org/scheme-7158/ The dark blue is the one to definitely use. I do not want it looking to feminine. I do want different colors for the 5 elements: Purpose, Mental, Physical, Emotional, Social.

Target Market(s)

Working professionals.

Font styles to use
Serif
Other font styles liked:
• Playfair Display

Requirements
Must have
• 4 Overlapping circles with one circle in center that says Purpose
Other 4 circles labeled Physical, Emotional, Mental, Social
Mandala-like design

**I added an attachment with colors I use when marketing this course.**
Nice to have
• Playfair Display font

```html
<!DOCTYPE html>
<html lang="en">
<head>
<meta charset="UTF-8">
<title>Ecosystem of Well-Being</title>
<link rel="stylesheet" href="https://fonts.googleapis.com/css2?family=Playfair+Display:wght@600;700&display=swap">
<style>
  :root {
    --ink: #0f1330;
    --paper: #ffffff;
    --physical: #e0874f;
    --mental: #bcd07e;
    --emotional: #8ec5da;
    --social: #c9443a;
    --purpose: #4f7fb8;
    --label: #ffffff;
  }
  html, body {
    margin: 0;
    padding: 0;
    width: 1166px;
    height: 1200px;
    overflow: hidden;
    background: var(--paper);
  }
  .wellbeing-mandala {
    display: block;
    width: 1166px;
    height: 1200px;
  }
  .ring-outline {
    fill: none;
    stroke: var(--ink);
    stroke-width: 3.5;
  }
  .element {
    opacity: 0.82;
  }
  .element--physical { fill: var(--physical); }
  .element--mental { fill: var(--mental); }
  .element--emotional { fill: var(--emotional); }
  .element--social { fill: var(--social); }
  .element-outline {
    fill: none;
    stroke: var(--ink);
    stroke-width: 3.5;
  }
  .purpose-core {
    fill: var(--purpose);
    opacity: 0.55;
  }
  .element-label {
    fill: var(--label);
    font-family: "Playfair Display", Georgia, serif;
    font-weight: 700;
    font-size: 42px;
    letter-spacing: 3px;
  }
  .purpose-label {
    fill: var(--label);
    font-family: "Playfair Display", Georgia, serif;
    font-weight: 600;
    font-size: 44px;
    letter-spacing: 1px;
  }
</style>
</head>
<body>
<svg class="wellbeing-mandala" viewBox="0 0 1034 1064" xmlns="http://www.w3.org/2000/svg" role="img" aria-label="Ecosystem of Well-Being: Physical, Mental, Emotional and Social circles overlapping around Purpose">
  <defs>
    <path id="arc-physical" d="M242.5 430 A158 158 0 0 1 450.2 229.5"/>
    <path id="arc-mental" d="M633.6 222.4 A158 158 0 0 1 816.6 405.4"/>
    <path id="arc-emotional" d="M196.7 629.7 A180 180 0 0 0 503.5 786"/>
    <path id="arc-social" d="M642.7 840.3 A180 180 0 0 0 851.3 631.7"/>
  </defs>

  <g class="mandala-rings">
    <circle class="ring-outline" cx="534" cy="320" r="202"/>
    <circle class="ring-outline" cx="323" cy="528" r="202"/>
    <circle class="ring-outline" cx="725" cy="528" r="202"/>
    <circle class="ring-outline" cx="534" cy="720" r="202"/>
  </g>

  <g class="elements">
    <circle class="element element--social" cx="674" cy="663" r="201"/>
    <circle class="element element--physical" cx="391" cy="376" r="201"/>
    <circle class="element element--emotional" cx="374" cy="661" r="201"/>
    <circle class="element element--mental" cx="661" cy="378" r="201"/>
  </g>

  <circle class="purpose-core" cx="534" cy="530" r="156"/>

  <g class="element-outlines">
    <circle class="element-outline" cx="391" cy="376" r="201"/>
    <circle class="element-outline" cx="661" cy="378" r="201"/>
    <circle class="element-outline" cx="374" cy="661" r="201"/>
    <circle class="element-outline" cx="674" cy="663" r="201"/>
  </g>

  <text class="element-label"><textPath href="#arc-physical" startOffset="50%" text-anchor="middle">PHYSICAL</textPath></text>
  <text class="element-label"><textPath href="#arc-mental" startOffset="50%" text-anchor="middle">MENTAL</textPath></text>
  <text class="element-label"><textPath href="#arc-emotional" startOffset="50%" text-anchor="middle">EMOTIONAL</textPath></text>
  <text class="element-label"><textPath href="#arc-social" startOffset="50%" text-anchor="middle">SOCIAL</textPath></text>

  <text class="purpose-label" x="532" y="538" text-anchor="middle" textLength="226" lengthAdjust="spacingAndGlyphs">PURPOSE</text>
</svg>
</body>
</html>
```